Logo & Stationery Design

We are a new company based in Sydney, Australia called Brivana Fresh Pantry. We import and distribute top quality olive oil to restaurants and deli's, etc.
We need a logo design, business cards and letterheads for our company.
For the logo we would like to see designs that include an olive branch (olives and leaves) and that include the colours green and purple. Please see examples attached.
We would like a health, wellness and nature feel in the design.
For the business cards and letterheads we would like to add an illustration with a tag line. We would like to see something along the lines of oil dripping from an olive into a champagne glass with the tag line "first press"

```html
<!DOCTYPE html>
<html lang="en">
<head>
<meta charset="utf-8">
<title>Brivana Fresh Pantry – Logo &amp; Stationery</title>
<link href="https://fonts.googleapis.com/css2?family=Quicksand:wght@400;500&display=swap" rel="stylesheet">
<style>
  :root {
    --olive-deep: #3f5a14;
    --olive: #6e8c1c;
    --olive-dark: #41600d;
    --lime: #c4d430;
    --lime-soft: #dfe7b8;
    --ink: #3a3a3a;
    --paper: #ffffff;
    --canvas: #ffffff;
  }
  * { box-sizing: border-box; margin: 0; padding: 0; }
  html, body { width: 1200px; height: 1000px; overflow: hidden; background: var(--canvas); }
  body { position: relative; font-family: "Quicksand", sans-serif; color: var(--ink); }

  .brand-mark { position: absolute; }
  .brand-mark .dot { position: absolute; left: 205px; top: 48px; width: 100px; height: 100px; border-radius: 50%; background: var(--olive); }
  .brand-mark .wordmark { position: absolute; left: 34px; top: 164px; font-size: 45px; font-weight: 400; color: var(--olive-deep); white-space: nowrap; letter-spacing: 0.6px; }

  .card { position: absolute; left: 48px; width: 464px; height: 258px; overflow: hidden; box-shadow: 0 1px 4px rgba(0,0,0,0.25); background: var(--paper); }
  .card--green { top: 318px; }
  .card--white { top: 638px; }
  .card svg.card-bg { position: absolute; inset: 0; }
  .card .tagline { position: absolute; left: 44px; top: 67px; font-size: 16px; white-space: nowrap; }
  .card--green .tagline { color: var(--olive); }
  .card--white .tagline { color: #ffffff; }
  .card .details { position: absolute; left: 190px; width: 254px; text-align: center; }
  .card .mini-dot { width: 34px; height: 34px; border-radius: 50%; margin: 0 auto 18px; }
  .card .company { font-size: 18px; line-height: 22px; white-space: nowrap; }
  .card .person { font-size: 22px; line-height: 28px; margin-top: 24px; }
  .card .role { font-size: 15px; line-height: 18px; margin-top: 0; }
  .card .contact { font-size: 11.5px; line-height: 14.6px; margin-top: 26px; white-space: nowrap; }
  .card--green .details { top: 20px; }
  .card--green .mini-dot { background: var(--lime); }
  .card--green .company { color: var(--lime-soft); }
  .card--green .person { color: #ffffff; }
  .card--green .role, .card--green .contact { color: var(--lime-soft); }
  .card--white .details { top: 24px; }
  .card--white .mini-dot { background: var(--olive); }
  .card--white .company { color: var(--olive-deep); }
  .card--white .person { color: var(--olive-deep); }
  .card--white .role { color: var(--olive); }
  .card--white .contact { color: var(--olive); }

  .letterhead { position: absolute; left: 563px; top: 55px; width: 587px; height: 837px; background: var(--paper); box-shadow: 0 1px 5px rgba(0,0,0,0.3); overflow: hidden; }
  .letterhead svg.sheet-lines { position: absolute; inset: 0; }
  .letterhead .head { position: absolute; left: 160px; top: 20px; width: 268px; text-align: center; }
  .letterhead .head .mini-dot { width: 34px; height: 34px; border-radius: 50%; background: var(--olive); margin: 0 auto 18px; }
  .letterhead .head .company { font-size: 18px; color: var(--olive-deep); white-space: nowrap; }
  .letterhead .head .contact { font-size: 9.5px; line-height: 11.5px; color: var(--olive); margin-top: 7px; white-space: nowrap; }
  .letterhead .salutation { position: absolute; left: 57px; top: 167px; font-size: 10px; }
  .letterhead .body { position: absolute; left: 57px; top: 221px; width: 473px; font-size: 9.6px; line-height: 13.3px; text-align: justify; }
  .letterhead .body p { margin-bottom: 11px; }
  .letterhead .tagline { position: absolute; left: 508px; top: 744px; font-size: 9px; color: var(--olive); white-space: nowrap; }
  .art { position: absolute; }
</style>
</head>
<body>

  <div class="brand-mark">
    <div class="dot"></div>
    <div class="wordmark">Brivana Fresh Pantry</div>
  </div>

  <section class="card card--green">
    <svg class="card-bg" width="464" height="258" viewBox="0 0 464 258">
      <path d="M92 0 C205 60 212 190 128 258 L464 258 L464 0 Z" fill="var(--olive)"/>
      <path d="M104 0 C214 62 220 192 140 258" fill="none" stroke="var(--lime)" stroke-width="6"/>
    </svg>
    <div class="art" role="img" aria-label="Illustration: olive sprig dripping oil into a cocktail glass" style="left:0;top:0;width:72px;height:70px;border-radius:0 0 40px 0;background:radial-gradient(circle at 40% 40%,#a9c235,#4f6e12);"></div>
    <div class="art" role="img" aria-label="Illustration: cocktail glass filled with olive oil" style="left:12px;top:90px;width:150px;height:160px;border-radius:4px 4px 60px 60px;background:linear-gradient(180deg,#c9dc3a,#8fa51f 60%,#6e8c1c);"></div>
    <div class="tagline">first press</div>
    <div class="details">
      <div class="mini-dot"></div>
      <div class="company">Brivana Fresh Pantry</div>
      <div class="person">Marcus Ellery</div>
      <div class="role">General Manager</div>
      <div class="contact">Harbour View Rooms, 218 Pitt Street, Sydney<br>phone: 02 8140 3376 • fax: 02 8140 3377<br>e-mail: hello@brivana-fresh.au<br>www.brivana-fresh.au</div>
    </div>
  </section>

  <section class="card card--white">
    <svg class="card-bg" width="464" height="258" viewBox="0 0 464 258">
      <defs>
        <linearGradient id="cardSweep" x1="0" y1="0" x2="1" y2="0">
          <stop offset="0" stop-color="#a6c22a"/>
          <stop offset="1" stop-color="var(--olive-dark)"/>
        </linearGradient>
      </defs>
      <path d="M0 0 L292 0 C190 55 150 180 160 258 L0 258 Z" fill="url(#cardSweep)"/>
      <path d="M300 0 C200 58 162 180 172 258" fill="none" stroke="var(--lime)" stroke-width="5"/>
    </svg>
    <div class="art" role="img" aria-label="Illustration: olive sprig dripping oil into a cocktail glass" style="left:0;top:0;width:72px;height:70px;border-radius:0 0 40px 0;background:radial-gradient(circle at 40% 40%,#b5cc3a,#4f6e12);"></div>
    <div class="art" role="img" aria-label="Illustration: cocktail glass filled with olive oil" style="left:14px;top:90px;width:150px;height:160px;border-radius:4px 4px 60px 60px;background:linear-gradient(180deg,#d4e25a,#a8bf2c 60%,#7d9a20);"></div>
    <div class="tagline">first press</div>
    <div class="details">
      <div class="mini-dot"></div>
      <div class="company">Brivana Fresh Pantry</div>
      <div class="person">Marcus Ellery</div>
      <div class="role">General Manager</div>
      <div class="contact">Harbour View Rooms, 218 Pitt Street, Sydney<br>phone: 02 8140 3376 • fax: 02 8140 3377<br>e-mail: hello@brivana-fresh.au<br>www.brivana-fresh.au</div>
    </div>
  </section>

  <section class="letterhead">
    <svg class="sheet-lines" width="587" height="837" viewBox="0 0 587 837">
      <path d="M150 128 Q330 205 587 66 L587 74 Q330 216 150 128 Z" fill="var(--lime)"/>
      <path d="M352 837 Q420 715 587 690" fill="none" stroke="var(--lime)" stroke-width="2"/>
    </svg>
    <div class="head">
      <div class="mini-dot"></div>
      <div class="company">Brivana Fresh Pantry</div>
      <div class="contact">Harbour View Rooms, 218 Pitt Street, Sydney<br>phone: 02 8140 3376 • fax: 02 8140 3377<br>e-mail: hello@brivana-fresh.au<br>www.brivana-fresh.au</div>
    </div>
    <div class="salutation">Dear, customer!</div>
    <div class="body">
      <p>Ullam quis enim dolor sit amet, velit esse modo tincidunt, nostrud aliquip magna, sed.</p>
      <p>Accumsan dolore feugiat nulla facilisis at vero eros et iusto odio dignissim qui blandit praesent luptatum zzril delenit augue duis dolore te feugait nulla facilisi. Nam liber tempor cum soluta nobis eleifend option congue nihil imperdiet doming id quod mazim placerat facer possim assum. Typi non habent claritatem insitam, est usus legentis in iis qui facit eorum claritatem. Investigationes demonstraverunt lectores legere me lius quod ii legunt saepius. Claritas est etiam processus dynamicus, qui sequitur mutationem consuetudium lectorum. Mirum est notare quam littera gothica, quam nunc putamus parum claram, anteposuerit litterarum formas humanitatis.</p>
      <p>Sed ut perspiciatis unde omnis iste natus error sit voluptatem accusantium doloremque laudantium, totam rem aperiam eaque ipsa quae ab illo inventore veritatis et quasi architecto beatae vitae dicta sunt explicabo nemo enim ipsam.</p>
      <p>Quis autem vel eum iure reprehenderit qui in ea voluptate velit esse quam nihil molestiae consequatur, vel illum dolorem.</p>
      <p>At vero eos et accusamus et iusto odio dignissimos ducimus qui blanditiis praesentium voluptatum deleniti atque corrupti quos dolores et quas molestias excepturi sint occaecati cupiditate non provident, similique sunt in culpa qui officia deserunt mollitia animi, id est laborum et dolorum fuga. Et harum quidem rerum facilis est et expedita distinctio. Nam libero tempore, cum soluta nobis est eligendi optio cumque nihil impedit quo minus id quod maxime placeat facere possimus, omnis voluptas assumenda est, omnis dolor repellendus. Temporibus autem quibusdam et aut officiis debitis aut rerum necessitatibus saepe eveniet ut et voluptates repudiandae sint et molestiae non recusandae. Itaque earum rerum hic tenetur a sapiente delectus, ut aut reiciendis voluptatibus maiores alias consequatur aut perferendis doloribus asperiores repellat.</p>
      <p>Nulla facilisi morbi tempus iaculis urna id volutpat lacus laoreet non curabitur gravida arcu ac tortor.</p>
    </div>
    <div class="art" role="img" aria-label="Illustration: olive sprig dripping oil" style="left:537px;top:664px;width:50px;height:70px;border-radius:30px 0 0 30px;background:radial-gradient(circle at 45% 45%,#a9c235,#4f6e12);"></div>
    <div class="tagline">first press</div>
    <div class="art" role="img" aria-label="Illustration: cocktail glass filled with olive oil" style="left:480px;top:758px;width:90px;height:79px;border-radius:2px 2px 30px 30px;background:linear-gradient(180deg,#c9dc3a,#8fa51f 60%,#6e8c1c);"></div>
  </section>

</body>
</html>
```